Letterhead for 3 attorney Workers' Comp law firm

We are a 3 attorney law office. We specialize in Workers' Compensation. Our office represents workers who are injured on the job, and the estates of workers who are killed one the job.
When we started our office, we created our own letterhead & have been using it for years. We've just recently hired the 3rd attorney, and were going to just add his name to the letterhead, but have decided we wanted to get a professionally designed letterhead and business cards at this point.
We want something that looks clean and professional. It must look good in black and white because we often make multiple copies of our documents. We're hoping for a design that resonates confidence, reliability and experience.
The design must include the firm name: Dorrance & Pike, PLLC. We would like the PLLC to be small compared to the Dorrance & Pike graphic. We also want to incorporate the attorney names: Ulric Dorrance, Janet Pike, and Lyle Hagberg. Our current letterhead has our contact info in the footer at the bottom of the page. We like that design, but are open to the idea of having it at the top. We'll leave that at the discretion of the designer. Our contact info is as follows: 472 S. Larchmont Avenue, Suite 315 Bellingham, WA 98117 Phone: 360-514-2967, Fax: 360-521-6079, and our website: www.dorrancepike-law.example
Target Market(s)
Clients, courts, other legal offices, doctors offices. These are the people who see our letterhead most frequently. It's not so much for marketing purposes, mainly so that we have a professional image when sending out documents.
Industry/Entity Type
Law Firm
Contact Information for Business Card
On the back of the business card: it can be designed, or be a template for filling in appointment reminder information (i.e. date, time, etc)
Colors
Designer to choose colors to be used in the design.
Requirements
Must have
- Must have our firm name at the top.
- Must include the attorney names.
- Must have all of our contact information (can be at top or bottom - whatever looks best with the design)
Nice to have
- A strong, confident design
Should not have
- We don't want the design to be playful, cartoony or busy.

```html
<!DOCTYPE html>
<html lang="en">
<head>
<meta charset="utf-8">
<title>Dorrance &amp; Pike, PLLC — Stationery</title>
<link rel="stylesheet" href="https://fonts.googleapis.com/css2?family=Questrial&family=Arimo:wght@400&display=swap">
<style>
  :root {
    --ink: #0b0b0b;
    --paper: #ffffff;
    --backdrop: #ececec;
    --reverse: #f2f2f2;
    --muted: #3a3a3a;
    --edge: #d2d2d2;
  }
  * { margin: 0; padding: 0; box-sizing: border-box; }
  html, body { width: 1200px; height: 1200px; overflow: hidden; }
  body {
    background: var(--backdrop);
    position: relative;
    font-family: "Arimo", Arial, sans-serif;
    color: var(--ink);
    -webkit-font-smoothing: antialiased;
    -moz-osx-font-smoothing: grayscale;
    font-smooth: always;
  }
  address { font-style: normal; }

  /* Firm name lockup: one line of type, a plain rule beneath */
  .lockup { position: absolute; display: block; }
  .lockup__name {
    display: block;
    font-family: "Questrial", "Helvetica Neue", sans-serif;
    font-weight: 400;
    line-height: 1;
    white-space: nowrap;
  }
  .lockup__rule { display: block; height: 1px; background: currentColor; }
  .lockup__suffix {
    position: absolute;
    font-family: "Questrial", "Helvetica Neue", sans-serif;
    font-size: 7px;
    letter-spacing: 0.5px;
    line-height: 1;
  }

  /* Letterhead */
  .letterhead { position: absolute; left: 218px; top: 342px; width: 382px; height: 510px; background: var(--paper); border: 1px solid var(--edge); }
  .letterhead__header { position: absolute; left: 0; top: 0; width: 100%; height: 54px; background: var(--ink); color: var(--reverse); }
  .letterhead .lockup { left: 14px; top: 17px; width: 132px; color: var(--reverse); }
  .letterhead .lockup__name { font-size: 15px; }
  .letterhead .lockup__rule { margin-top: 4px; }
  .letterhead__contact { position: absolute; left: 272px; top: 9px; font-size: 5px; line-height: 6.6px; color: var(--reverse); }
  .letterhead__footer { position: absolute; left: 0; bottom: 24px; width: 100%; text-align: center; font-size: 7px; letter-spacing: 2.2px; color: var(--ink); }

  /* Business cards */
  .card { position: absolute; width: 333px; height: 203px; }
  .card--front { left: 657px; top: 363px; background: var(--ink); color: var(--reverse); }
  .card--back { left: 657px; top: 615px; background: var(--paper); border: 1px solid var(--edge); color: var(--ink); }

  .card .lockup { left: 52px; width: 238px; }
  .card--front .lockup { top: 78px; }
  .card--back .lockup { top: 38px; }
  .card .lockup__name { font-size: 24px; }
  .card .lockup__rule { margin-top: 5px; }
  .card .lockup__suffix { right: 0; top: 14px; }

  .card__attorneys { position: absolute; left: 52px; font-size: 6px; line-height: 7.4px; }
  .card--front .card__attorneys { top: 113px; color: var(--reverse); }
  .card--back .card__attorneys { top: 73px; color: var(--muted); }

  .card__web { position: absolute; font-size: 7px; letter-spacing: 2.2px; white-space: nowrap; }
  .card--front .card__web { left: 0; width: 100%; bottom: 16px; text-align: center; color: var(--reverse); }
  .card--back .card__web { right: 10px; bottom: 7px; color: var(--reverse); font-size: 6px; letter-spacing: 1.8px; }

  .card__contact { position: absolute; left: 180px; top: 129px; font-size: 7.4px; line-height: 8.6px; color: var(--ink); }
  .card__stripe { position: absolute; left: 0; bottom: 0; width: 331px; height: 30px; }
</style>
</head>
<body>

<section class="letterhead" aria-label="Letterhead">
  <header class="letterhead__header">
    <span class="lockup">
      <span class="lockup__name">Dorrance &amp; Pike</span>
      <span class="lockup__rule"></span>
    </span>
    <address class="letterhead__contact">
      472 S. Larchmont Avenue<br>
      Suite 315 Bellingham, WA 98117<br>
      Phone: 360-514-2967<br>
      Fax: 360-521-6079<br>
      Website: www.dorrancepike-law.example
    </address>
  </header>
  <footer class="letterhead__footer">www.dorrancepike-law.example</footer>
</section>

<section class="card card--front" aria-label="Business card front">
  <span class="lockup">
    <span class="lockup__name">Dorrance &amp; Pike</span>
    <span class="lockup__rule"></span>
    <span class="lockup__suffix">PLLC</span>
  </span>
  <p class="card__attorneys">Ulric Dorrance, Janet Pike<br>&amp; Lyle Hagberg</p>
  <p class="card__web">www.dorrancepike-law.example</p>
</section>

<section class="card card--back" aria-label="Business card back">
  <span class="lockup">
    <span class="lockup__name">Dorrance &amp; Pike</span>
    <span class="lockup__rule"></span>
    <span class="lockup__suffix">PLLC</span>
  </span>
  <p class="card__attorneys">Ulric Dorrance, Janet Pike<br>&amp; Lyle Hagberg</p>
  <address class="card__contact">
    472 S. Larchmont Avenue<br>
    Suite 315 Bellingham, WA 98117<br>
    Phone: 360-514-2967<br>
    Fax: 360-521-6079
  </address>
  <svg class="card__stripe" viewBox="0 0 331 30" aria-hidden="true">
    <path d="M150 30 L150 26 Q158 26 164 20 Q170 14 180 14 L331 14 L331 30 Z" fill="#0b0b0b"/>
    <path d="M0 20 L142 20 Q150 20 156 14 Q162 8 172 8 L331 8" fill="none" stroke="#0b0b0b" stroke-width="2.4"/>
    <path d="M0 26 L144 26" fill="none" stroke="#0b0b0b" stroke-width="2.4"/>
  </svg>
  <p class="card__web">www.dorrancepike-law.example</p>
</section>

</body>
</html>
```